PDF to help promote my website to potential advertisers

I need a one page PDF that may be used on our site to help promote my website (LKPhomes.com) to potential advertisers. It's a pretty simple document but needs to make it look great.

I've provided the audience info. I'm hoping to have this look sorta like the Market Ledger's advertising page: http://www.marketledger-example.com/advertise

It's not rocket science but I hope you can help.

Target Market(s)

Potential Advertisers are typically home improvement-related-services like contractors and home builders. Also real estate agents and home-sales related services.

Industry/Entity Type

Media

Colors

Designer to choose colors to be used in the design.

Requirements
Must have
• I want the graphics to make the audience info (in the txt file) stand out. Needs to be similar to this: http://www.marketledger-example.com/advertise.
• I want to use the PDF to send via email to prospective clients and also post on our website, so it has to be able to work almost like graphics on a site. I may have it printed as well.
Nice to have
• Colors and logo and font should match our site. Please grab the logo and/font info from our site

```html
<!DOCTYPE html>
<html lang="en">
<head>
<meta charset="utf-8">
<title>Advertising with LKPhomes</title>
<link rel="stylesheet" href="https://fonts.googleapis.com/css2?family=Roboto+Condensed:wght@300;400;700&family=Roboto:wght@400;700&display=swap">
<style>
  :root {
    --charcoal: #2f2f31;
    --panel: rgba(47, 47, 49, 0.93);
    --brand-blue: #3f8fd8;
    --band-blue: #4a86cb;
    --ink-dark: #2a2a2c;
    --white: #ffffff;
    --grey-name: #9c9c9c;
    --stage: #e9edf1;
  }
  * { box-sizing: border-box; margin: 0; padding: 0; }
  html, body { width: 1200px; height: 1200px; overflow: hidden; }
  body {
    background: var(--stage);
    font-family: "Roboto Condensed", "Arial Narrow", sans-serif;
    color: var(--white);
    position: relative;
  }
  .flyer {
    position: absolute; left: 134px; top: 0;
    width: 932px; height: 1200px;
    background: var(--charcoal);
    overflow: hidden;
  }
  .abs { position: absolute; }

  /* Header */
  .header { left: 0; top: 0; width: 932px; height: 122px; background: var(--charcoal); }
  .brand-mark { left: 468px; top: 48px; width: 54px; height: 54px; background: var(--brand-blue); }
  .brand-name {
    left: 538px; top: 44px;
    font-family: "Roboto Condensed", sans-serif; font-weight: 700;
    font-size: 58px; line-height: 62px; letter-spacing: 1px;
    color: var(--grey-name);
  }

  /* Hero photo area */
  .hero-photo {
    left: 0; top: 122px; width: 932px; height: 598px;
    background: linear-gradient(180deg, #3b73c4 0%, #5e92d8 45%, #8fb3df 68%, #6b8f3e 88%, #4d7a2a 100%);
  }
  .hero-house {
    left: 0; top: 122px; width: 410px; height: 598px;
    background: linear-gradient(180deg, #9a5a4a 0%, #b06a52 45%, #5d6f8a 75%, #567a2f 100%);
  }
  .tagline {
    left: 410px; top: 138px; width: 470px; text-align: center;
    font-weight: 300; font-size: 41px; line-height: 50px;
  }
  .promo-shape { left: 0; top: 0; }
  .promo-title {
    left: 410px; top: 382px; width: 478px; text-align: center;
    font-weight: 700; font-size: 66px; line-height: 72px; letter-spacing: 1px;
  }
  .promo-with {
    left: 410px; top: 462px; width: 478px; text-align: center;
    font-size: 40px; line-height: 44px;
  }
  .promo-name {
    left: 410px; top: 514px; width: 478px; text-align: center;
    font-weight: 700; font-size: 60px; line-height: 64px; color: var(--grey-name);
  }
  .promo-copy {
    left: 442px; top: 600px; width: 412px;
    font-size: 20px; line-height: 32px; text-align: justify; text-align-last: justify;
  }
  .promo-copy strong { font-weight: 700; font-size: 25px; }

  /* Audience stats */
  .about-title {
    left: 46px; top: 774px;
    font-weight: 700; font-size: 41px; line-height: 46px; color: var(--brand-blue);
  }
  .reach-lead { left: 240px; top: 822px; width: 156px; text-align: right; font-size: 20px; }
  .channel-dots { left: 412px; top: 780px; }
  .reach-number {
    left: 498px; top: 780px;
    font-weight: 700; font-size: 72px; line-height: 76px;
  }
  .reach-note { left: 655px; top: 790px; width: 250px; font-size: 14px; line-height: 18px; }
  .stat { display: flex; align-items: center; }
  .stat-value { font-weight: 700; font-size: 39px; line-height: 44px; width: 86px; flex: none; }
  .stat-label { font-size: 20px; line-height: 25px; }
  .col-left { left: 48px; }
  .col-right { left: 410px; }

  /* Listing band */
  .listing-band {
    left: 0; top: 1077px; width: 932px; height: 123px;
    background: var(--band-blue); color: var(--ink-dark); text-align: center;
  }
  .listing-band h2 {
    font-family: "Roboto", sans-serif; font-weight: 700;
    font-size: 24px; line-height: 28px; margin-top: 7px;
  }
  .listing-band p { font-size: 17px; line-height: 22px; }
  .listing-url {
    font-family: "Roboto", sans-serif; font-weight: 700;
    font-size: 46px; line-height: 54px;
  }
</style>
</head>
<body>
  <main class="flyer">
    <header class="header abs">
      <div class="brand-mark abs"></div>
      <div class="brand-name abs">LKPHOMES</div>
    </header>

    <div class="hero-photo abs" role="img" aria-label="Photo of a smiling family standing on a lawn in front of a red brick suburban house under a blue sky"></div>
    <div class="hero-house abs" role="img" aria-label="Red brick house and family in the foreground"></div>

    <p class="tagline abs">Obsessed with great homes around Milwaukee</p>

    <svg class="promo-shape abs" width="932" height="1200" viewBox="0 0 932 1200" aria-hidden="true">
      <polygon points="410,378 655,280 888,378 888,720 410,720" fill="rgba(47,47,49,0.93)"/>
      <polyline points="410,382 655,296 888,384" fill="none" stroke="#4a86cb" stroke-width="4"/>
    </svg>

    <h1 class="promo-title abs">ADVERTISING</h1>
    <div class="promo-with abs">with</div>
    <div class="promo-name abs">LKPHOMES</div>
    <p class="promo-copy abs">Learn how you can partner with us to reach our <strong>Milwaukee audience who desire to move and/or renovate their homes.</strong></p>

    <h2 class="about-title abs">About LKPhomes.com</h2>
    <div class="reach-lead abs">We reach over</div>
    <svg class="channel-dots abs" width="76" height="74" viewBox="0 0 76 74" aria-hidden="true">
      <circle cx="18" cy="18" r="16" fill="none" stroke="#fff" stroke-width="3"/>
      <circle cx="56" cy="18" r="16" fill="none" stroke="#fff" stroke-width="3"/>
      <circle cx="18" cy="55" r="16" fill="none" stroke="#fff" stroke-width="3"/>
      <circle cx="56" cy="55" r="16" fill="none" stroke="#fff" stroke-width="3"/>
    </svg>
    <div class="reach-number abs">1000</div>
    <p class="reach-note abs">readers each day through our website, our Friendbook Page, our Snapgram and our email newsletter.</p>

    <div class="stat abs col-left" style="top:882px"><span class="stat-value">67%</span><span class="stat-label">are women</span></div>
    <div class="stat abs col-left" style="top:947px"><span class="stat-value">75%</span><span class="stat-label">in milwaukee area</span></div>
    <div class="stat abs col-left" style="top:1011px"><span class="stat-value">30%</span><span class="stat-label">do not have an agent</span></div>

    <div class="stat abs col-right" style="top:880px"><span class="stat-value">55%</span><span class="stat-label">in the prime home purchase age range of 25-44</span></div>
    <div class="stat abs col-right" style="top:940px"><span class="stat-value">60%</span><span class="stat-label">claim they are "happy but looking"<br>for a future new home</span></div>
    <div class="stat abs col-right" style="top:1013px"><span class="stat-value">55%</span><span class="stat-label">plan to do a home improvement projects<br>in the next year</span></div>

    <footer class="listing-band abs">
      <h2>SUBMIT YOUR LISTING:</h2>
      <p>To find out more about how to get your listing or your For Sale By Owner listing on LKPhomes</p>
      <div class="listing-url">www.LKPhomes.com</div>
    </footer>
  </main>
</body>
</html>
```